Bravel Acres Business Cards

design business cards for our new business should match my Corvane Quotations business cards

Contact Information for Business Card

2817 W 68th N St
Tulsa, OK 74592

Requirements
Must have
• should match logo colors

```html
<!DOCTYPE html>
<html lang="en">
<head>
<meta charset="utf-8">
<title>Bravel Acres Business Cards</title>
<link href="https://fonts.googleapis.com/css2?family=Montserrat:wght@400;500;600;700&display=swap" rel="stylesheet">
<style>
  :root {
    --backdrop: #2f2f2f;
    --leaf-green: #7bc043;
    --mid-green: #45b77a;
    --teal: #1aa9b5;
    --ink: #10303a;
    --text: #333333;
    --rule: #d6d6d6;
    --paper: #ffffff;
  }
  * { margin: 0; padding: 0; box-sizing: border-box; }
  html, body {
    width: 1200px; height: 866px; overflow: hidden;
    background: var(--backdrop);
    font-family: "Montserrat", Arial, sans-serif;
  }
  .sheet {
    width: 1200px; height: 866px;
    display: flex; align-items: center; justify-content: center; gap: 48px;
  }
  .card {
    width: 520px; height: 298px; position: relative; overflow: hidden;
    box-shadow: 0 10px 24px rgba(0,0,0,.45);
  }
  .card-front {
    background: linear-gradient(120deg, var(--leaf-green) 0%, var(--mid-green) 50%, var(--teal) 100%);
    display: flex; align-items: center; justify-content: center;
  }
  .brand {
    display: flex; align-items: center; gap: 12px;
    font-weight: 600; letter-spacing: 6px; text-transform: uppercase;
  }
  .brand-dot { width: 14px; height: 14px; border-radius: 50%; }
  .card-front .brand { color: var(--paper); font-size: 34px; }
  .card-front .brand-dot { background: var(--paper); }
  .card-back { background: var(--paper); }
  .card-back .brand {
    position: absolute; right: 28px; top: 96px;
    color: var(--ink); font-size: 24px; letter-spacing: 4px;
  }
  .card-back .brand-dot { background: var(--teal); width: 11px; height: 11px; }
  .contact { position: absolute; left: 28px; top: 60px; }
  .person-name {
    color: var(--leaf-green); font-weight: 700; font-size: 15px;
    letter-spacing: 1px; text-transform: uppercase;
  }
  .person-role { color: var(--text); font-size: 12px; margin-bottom: 10px; }
  .contact-list { list-style: none; font-size: 11.5px; color: var(--text); }
  .contact-list li { display: flex; align-items: center; gap: 7px; line-height: 18px; }
  .contact-list svg { width: 11px; height: 11px; fill: var(--mid-green); flex: none; }
  .web-accent { color: var(--leaf-green); }
  .divider {
    position: absolute; left: 190px; right: 28px; top: 200px;
    border-top: 1px solid var(--rule);
  }
  .address {
    position: absolute; right: 28px; bottom: 34px;
    font-size: 12px; color: var(--text); line-height: 17px; text-align: left;
  }
</style>
</head>
<body>
<main class="sheet">
  <section class="card card-front">
    <div class="brand"><span class="brand-dot"></span>Bravel Acres</div>
  </section>

  <section class="card card-back">
    <div class="contact">
      <p class="person-name">Marcus Delane</p>
      <p class="person-role">Managing Director</p>
      <ul class="contact-list">
        <li><svg viewBox="0 0 24 24"><path d="M6.6 10.8a15 15 0 0 0 6.6 6.6l2.2-2.2a1 1 0 0 1 1-.25 11.4 11.4 0 0 0 3.6.57 1 1 0 0 1 1 1V20a1 1 0 0 1-1 1A17 17 0 0 1 3 4a1 1 0 0 1 1-1h3.5a1 1 0 0 1 1 1c0 1.25.2 2.45.57 3.57a1 1 0 0 1-.25 1z"/></svg>044-318 270 546</li>
        <li><svg viewBox="0 0 24 24"><path d="M7 1h10a2 2 0 0 1 2 2v18a2 2 0 0 1-2 2H7a2 2 0 0 1-2-2V3a2 2 0 0 1 2-2zm0 3v14h10V4zm5 15.5a1 1 0 1 0 0 2 1 1 0 0 0 0-2z"/></svg>044-318 270 547</li>
        <li><svg viewBox="0 0 24 24"><path d="M2 5h20v14H2zm2 2v.5l8 5 8-5V7l-8 5z"/></svg>hello@bravelacres.com</li>
        <li><svg viewBox="0 0 24 24"><path d="M12 2a10 10 0 1 0 0 20 10 10 0 0 0 0-20zm-1 2.1V11H5.1A7 7 0 0 1 11 4.1zm2 0A7 7 0 0 1 18.9 11H13zM5.1 13H11v6.9A7 7 0 0 1 5.1 13zm7.9 6.9V13h5.9a7 7 0 0 1-5.9 6.9z"/></svg>www.<span class="web-accent">bravelacres</span>.com</li>
      </ul>
    </div>
    <div class="brand"><span class="brand-dot"></span>Bravel Acres</div>
    <div class="divider"></div>
    <address class="address" style="font-style:normal">2817 W 68th N St<br>Tulsa, OK 74592</address>
  </section>
</main>
</body>
</html>
```